Business card for home decor store and design

I need a business card for my home decor boutique that’s professional looking boho/rustic. We sell vintage furniture, vintage finds, lamps, throws, rugs. We also carry a Diy paint line for refinishing furniture. We offer workshop on painting furniture, private or group setting. We in the heart of Old Town Red Bluff. We love to design, build and restore. Family owned small business. Our style is rustic boho farmhouse. We search for one of a kind found and repurposed items. We love vintage home decor, vintage windows.

Target Market(s)

Home decor

Industry/Entity Type

Home Accessories

Contact Information for Business Card

Have a rustic look/boho

Font styles to use
Serif
Script

Requirements
Must have
• Logo

```html
<!DOCTYPE html>
<html lang="en">
<head>
<meta charset="utf-8">
<title>Birch &amp; Loam Co. — Business Card</title>
<link href="https://fonts.googleapis.com/css2?family=Poppins:wght@300;400;500&family=Yellowtail&display=swap" rel="stylesheet">
<style>
  :root {
    --backdrop: #3a3a3c;
    --kraft: #b89c70;
    --kraft-dark: #a88c60;
    --ink: #141210;
    --paper-white: #fbf8f2;
    --faint: rgba(255, 250, 240, 0.16);
  }
  * { margin: 0; padding: 0; box-sizing: border-box; }
  html, body {
    width: 1200px;
    height: 965px;
    overflow: hidden;
    background: var(--backdrop);
    font-family: "Poppins", sans-serif;
  }
  .canvas { position: relative; width: 1200px; height: 965px; }

  .card {
    position: absolute;
    left: 270px;
    width: 660px;
    height: 377px;
    background: radial-gradient(circle at 40% 35%, var(--kraft) 0%, var(--kraft-dark) 100%);
    overflow: hidden;
    box-shadow: 0 8px 24px rgba(0,0,0,0.45);
  }
  .card--front { top: 70px; }
  .card--back { top: 518px; }

  /* front */
  .front-decor {
    position: absolute;
    left: 200px; top: 60px;
    width: 320px; height: 320px;
    border-radius: 50%;
    border: 18px solid var(--faint);
  }
  .brand {
    position: absolute;
    display: flex;
    align-items: center;
    gap: 14px;
    color: var(--ink);
    font-weight: 500;
    white-space: nowrap;
  }
  .brand__dot {
    border-radius: 50%;
    background: var(--ink);
    flex: none;
  }
  .card--front .brand {
    left: 50%; top: 50%;
    transform: translate(-50%, -50%);
    font-size: 40px;
  }
  .card--front .brand__dot { width: 26px; height: 26px; }

  /* back */
  .card--back .brand {
    left: 34px; top: 56px;
    font-size: 26px;
  }
  .card--back .brand__dot { width: 18px; height: 18px; }

  .rule {
    position: absolute;
    height: 1.5px;
    background: var(--paper-white);
  }
  .rule--top { left: 290px; right: 30px; top: 122px; }
  .rule--bottom { left: 30px; width: 360px; top: 236px; }

  .identity {
    position: absolute;
    left: 40px; right: 30px; top: 150px;
    height: 70px;
    display: flex;
    align-items: center;
    white-space: nowrap;
  }
  .name {
    font-family: "Yellowtail", "Brush Script MT", cursive;
    font-size: 44px;
    color: var(--ink);
    line-height: 1;
    flex: none;
  }
  .divider {
    width: 3px; height: 38px;
    margin: 0 16px 0 18px;
    background: var(--paper-white);
    flex: none;
  }
  .role {
    font-size: 17px;
    font-weight: 300;
    color: var(--paper-white);
    flex: none;
  }
  .address {
    margin-left: auto;
    padding-left: 20px;
    font-size: 15px;
    font-weight: 300;
    color: var(--paper-white);
    line-height: 1.4;
    flex: none;
  }
  .contacts {
    position: absolute;
    left: 44px; top: 262px;
    list-style: none;
  }
  .contacts li {
    display: flex;
    align-items: center;
    gap: 12px;
    font-size: 18px;
    font-weight: 300;
    color: var(--paper-white);
    line-height: 30px;
  }
  .contacts svg { width: 18px; height: 18px; flex: none; }
</style>
</head>
<body>
<main class="canvas">

  <section class="card card--front" aria-label="Business card front">
    <div class="front-decor" aria-hidden="true"></div>
    <div class="brand">
      <span class="brand__dot"></span>
      <span class="brand__name">Birch &amp; Loam Co.</span>
    </div>
  </section>

  <section class="card card--back" aria-label="Business card back">
    <div class="brand">
      <span class="brand__dot"></span>
      <span class="brand__name">Birch &amp; Loam Co.</span>
    </div>
    <div class="rule rule--top"></div>

    <div class="identity">
      <p class="name">Elsa Marlow</p>
      <span class="divider" aria-hidden="true"></span>
      <p class="role">Managing partner</p>
      <p class="address">Street 14, 5310 Linden<br>Florida</p>
    </div>

    <div class="rule rule--bottom"></div>

    <ul class="contacts">
      <li>
        <svg viewBox="0 0 24 24" aria-hidden="true"><path fill="#141210" d="M6.6 10.8a15 15 0 0 0 6.6 6.6l2.2-2.2a1 1 0 0 1 1-.25 11.4 11.4 0 0 0 3.6.6 1 1 0 0 1 1 1V20a1 1 0 0 1-1 1A17 17 0 0 1 3 4a1 1 0 0 1 1-1h3.5a1 1 0 0 1 1 1c0 1.25.2 2.45.6 3.6a1 1 0 0 1-.25 1z"/></svg>
        +1 530 555 0142
      </li>
      <li>
        <svg viewBox="0 0 24 24" aria-hidden="true"><rect x="2" y="5" width="20" height="14" fill="none" stroke="#141210" stroke-width="2"/><path d="M2 5l10 8 10-8" fill="none" stroke="#141210" stroke-width="2"/></svg>
        elsa@birchloam.com
      </li>
      <li>
        <svg viewBox="0 0 24 24" aria-hidden="true"><circle cx="12" cy="12" r="10" fill="#141210"/><path d="M2 12h20M12 2c3 3 3 17 0 20M12 2c-3 3-3 17 0 20" fill="none" stroke="#b89c70" stroke-width="1.3"/></svg>
        www.birchloam.com
      </li>
    </ul>
  </section>

</main>
</body>
</html>
```